BrivoPeak Business Card Design Project

We are looking for a modern, clean business card design for our new company. We are a consulting firm focused on the financial services market providing management and IT consulting to banks, insurance companies, etc. Please include our company logo and company contact information from the attached file in the design. Two versions of the logo are attached, either version is acceptable. Logos are available in other file formats if needed. We would like to include the contact information for both our UK and US offices as well as the following information for each individual card holder: Name, position/title, address, phone number and e-mail address.
Updates
Project Deadline Extended
Reason: A last minute trip over seas has prevented us from finalizing the decision. A decision will be made this week. We apologize for the inconvenience.
Industry/Entity Type
Business
Contact Information for Business Card
Company logo.
Company locations and phone numbers for both the US and UK offices.
Company URL.
Cardholder Name
Cardholder Position/title
Cardholder Address
Cardholder Phone Number
Cardholder e-mail Address
Look and feel
Each slider illustrates characteristics of the customer's brand and the style your logo design should communicate.

```html
<!DOCTYPE html>
<html lang="en">
<head>
<meta charset="utf-8">
<title>BrivoPeak – Business Card</title>
<link href="https://fonts.googleapis.com/css2?family=Exo+2:ital,wght@1,700&family=Montserrat:wght@400;500;600&display=swap" rel="stylesheet">
<style>
  :root {
    --navy: #2a3d63;
    --slate: #6a6c6e;
    --paper: #f7f8f8;
    --backdrop: #b9bbbc;
    --ink: #2b2b2b;
    --ink-light: #ffffff;
  }
  * { box-sizing: border-box; margin: 0; padding: 0; }
  html, body { width: 1200px; height: 895px; overflow: hidden; }
  body {
    background: var(--backdrop);
    display: flex;
    align-items: center;
    justify-content: center;
    gap: 40px;
    font-family: "Montserrat", sans-serif;
  }
  .card {
    position: relative;
    width: 560px;
    height: 320px;
    background: var(--paper);
    overflow: hidden;
    box-shadow: 0 6px 18px rgba(0,0,0,0.18);
  }
  .card-shapes { position: absolute; inset: 0; }

  .brand-name {
    position: absolute;
    display: flex;
    align-items: center;
    justify-content: center;
    gap: 10px;
    font-family: "Montserrat", sans-serif;
    font-weight: 600;
    font-size: 34px;
    color: var(--navy);
    line-height: 1;
  }
  .brand-mark {
    width: 16px;
    height: 16px;
    background: var(--slate);
    flex: none;
  }

  /* Brand side */
  .card-front .brand-name { left: 40px; top: 110px; width: 300px; }
  .website {
    position: absolute;
    left: 40px;
    top: 196px;
    width: 300px;
    text-align: center;
    font-size: 17px;
    font-weight: 500;
    color: var(--ink);
    letter-spacing: 0.5px;
  }

  /* Contact side */
  .holder { position: absolute; left: 38px; top: 22px; }
  .holder-name {
    font-family: "Exo 2", sans-serif;
    font-style: italic;
    font-weight: 700;
    font-size: 30px;
    color: var(--navy);
    letter-spacing: 1px;
    line-height: 1.1;
  }
  .holder-title {
    font-size: 9px;
    font-weight: 500;
    letter-spacing: 2px;
    color: #333;
    margin-top: 2px;
    padding-left: 30px;
  }
  .contact-list {
    position: absolute;
    left: 14px;
    top: 152px;
    list-style: none;
    color: var(--ink-light);
    font-size: 12px;
    line-height: 1.35;
  }
  .contact-item { display: flex; align-items: flex-start; gap: 10px; margin-bottom: 12px; }
  .contact-icon { width: 16px; height: 16px; flex: none; }
  .card-back .brand-name { left: 260px; top: 190px; width: 280px; }
</style>
</head>
<body>

  <section class="card card-back" aria-label="Contact side">
    <svg class="card-shapes" viewBox="0 0 560 320" aria-hidden="true">
      <polygon points="0,112 360,56 318,88 0,136" fill="var(--slate)"/>
      <polygon points="0,144 305,98 170,320 0,320" fill="var(--navy)"/>
    </svg>
    <div class="holder">
      <h1 class="holder-name">SAM CARTER</h1>
      <p class="holder-title">GENERAL MANAGER</p>
    </div>
    <ul class="contact-list">
      <li class="contact-item">
        <svg class="contact-icon" viewBox="0 0 16 16"><circle cx="8" cy="8" r="8" fill="#ffffff"/><path d="M5.4 4.2l1.4 1.6-.8 1.1c.6 1.3 1.5 2.2 2.8 2.8l1.1-.8 1.6 1.4-.9 1.4c-3-.4-5.6-3-6-6z" fill="var(--navy)"/></svg>
        <span>020 555 0147</span>
      </li>
      <li class="contact-item">
        <svg class="contact-icon" viewBox="0 0 16 16"><circle cx="8" cy="8" r="8" fill="#ffffff"/><rect x="4" y="5.2" width="8" height="5.6" fill="var(--navy)"/><path d="M4 5.2l4 3 4-3" stroke="#ffffff" stroke-width="0.8" fill="none"/></svg>
        <span>sam@brivopeak.com</span>
      </li>
      <li class="contact-item">
        <svg class="contact-icon" viewBox="0 0 16 16"><circle cx="8" cy="8" r="8" fill="#ffffff"/><path d="M8 3.5a3 3 0 0 1 3 3c0 2.2-3 6-3 6s-3-3.8-3-6a3 3 0 0 1 3-3z" fill="var(--navy)"/><circle cx="8" cy="6.5" r="1" fill="#ffffff"/></svg>
        <span>41 Harbour Street Level 9<br>London</span>
      </li>
    </ul>
    <p class="brand-name"><span class="brand-mark"></span>BrivoPeak</p>
  </section>

  <section class="card card-front" aria-label="Brand side">
    <svg class="card-shapes" viewBox="0 0 560 320" aria-hidden="true">
      <polygon points="345,0 402,0 418,320 392,320" fill="var(--slate)"/>
      <polygon points="402,0 560,0 560,320 418,320" fill="var(--navy)"/>
    </svg>
    <p class="brand-name"><span class="brand-mark"></span>BrivoPeak</p>
    <p class="website">www.brivopeakpartners.com</p>
  </section>

</body>
</html>
```